Womens Personal Training studio needs new year flyers

I need a double sided A5 flyer to attract Women / Mothers to my fitness business, Blossom Daily, in the new year.

My business colour is teal, I am located in Springwood QLD Aus

Exclusive studio training for women. At Blossom Daily we don't make New years resolutions, we Empower you to make the changes for life!

examples of pain Q's: Do you feel guilty about wanting to do something for yourself? Do you worry about what exercises are safe post baby? Are you struggling to regain control of your body and your life?

Would you like to love yourself and your body as much as you lvoe your baby?

I work with women to apporpriately and progressivley rebuild their bodies post preganany. As the Leading specialist in Pre and Post Natal Rehabilitation and Fitness in Logan, Corinne knows what it takes to find the right balance. With a vision of Empowering this generation to inspire the next, Corinne teaches skills for LIFE so you can lead your family to a Healthier, Fitter and Stronger future! Using a fusion of Pilates, Strength Conditioning and Cardio Corinne customises a plan for each individual. Your free consultation is waiting call now and learn the first steps to making the change Valued at $147 Don’t Miss out!! Corinne 0438 270 614

Quote to go with image "Corinne doesn't just help you achieve your weight loss goals she works with you to make sure you are 'Blossom Daily'." Maren Holt July 2013

Target Market(s)

Women / Mothers

Industry/Entity Type

Training

Requirements
Must have
• call to action
contact details
Corinne Ashby
0438 270 614
corinne@blossomdailystudio.net.au
www.blossomdailystudio.net.au

```html
<!DOCTYPE html>
<html lang="en">
<head>
<meta charset="utf-8">
<title>Blossom Daily – Pre and Post Natal Fitness Flyer</title>
<link rel="stylesheet" href="https://fonts.googleapis.com/css2?family=Lato:ital,wght@0,300;0,400;1,300;1,700&display=swap">
<style>
  :root {
    --teal: #4aa3ad;
    --white: #ffffff;
    --photo-placeholder: #6fb3bb;
    --shadow: rgba(0, 0, 0, 0.35);
  }
  * { margin: 0; padding: 0; box-sizing: border-box; }
  html, body { width: 846px; height: 1200px; overflow: hidden; }
  body {
    background: var(--teal);
    font-family: "Lato", Arial, sans-serif;
    color: var(--white);
    position: relative;
  }
  .before-after {
    position: absolute;
    left: 137px;
    top: 114px;
    width: 302px;
    height: 394px;
    background: var(--white);
    padding: 7px;
    display: flex;
    gap: 7px;
    transform: rotate(-1.6deg);
    box-shadow: 3px 5px 8px var(--shadow);
  }
  .before-after__photo {
    flex: 1;
    background: var(--photo-placeholder);
  }
  .testimonial {
    position: absolute;
    left: 479px;
    top: 141px;
    width: 227px;
  }
  .testimonial__quote {
    font-style: italic;
    font-weight: 700;
    font-size: 22.5px;
    line-height: 36.3px;
    text-align: justify;
    hyphens: auto;
    text-shadow: 1px 1px 2px var(--shadow);
  }
  .testimonial__author {
    margin-top: 12px;
    font-weight: 300;
    font-size: 22.5px;
    line-height: 30px;
    text-shadow: 1px 1px 2px var(--shadow);
  }
  .about {
    position: absolute;
    left: 140px;
    top: 558px;
    width: 566px;
    font-size: 22.3px;
    line-height: 36.4px;
    font-weight: 300;
    text-align: justify;
    text-shadow: 1px 1px 2px var(--shadow);
  }
  .about p + p { margin-top: 36.4px; }
  .about .cta {
    font-style: italic;
    font-weight: 700;
    font-size: 21.8px;
  }
  .cta__value { text-decoration: underline; }
</style>
</head>
<body>
  <div class="before-after">
    <div class="before-after__photo" role="img" aria-label="Before photo: client during pregnancy, standing side-on"></div>
    <div class="before-after__photo" role="img" aria-label="After photo: same client after post-natal training, standing side-on"></div>
  </div>

  <blockquote class="testimonial">
    <p class="testimonial__quote" lang="en">“Corinne doesn’t just help you achieve your weight loss goals she works with you to make sure you are ‘Blossom Daily’.”</p>
    <p class="testimonial__author">- Maren Holt July 2013</p>
  </blockquote>

  <section class="about">
    <p>I work with women to appropriately and progressivley rebuild their bodies post preganany. As the Leading specialist in Pre and Post Natal Rehabilitation and Fitness in Logan, Corinne knows what it takes to find the right balance.</p>
    <p>With a vision of Empowering this generation to inspire the next, Corinne teaches skills for LIFE so you can lead your family to a Healthier, Fitter and Stronger future! Using a fusion of Pilates, Strength Conditioning and Cardio Corinne customises a plan for each individual.</p>
    <p class="cta">Your free consultation is waiting call now and learn the first steps to making the change. <span class="cta__value">Valued at $147 Don’t Miss out!!</span><br>- Corinne 0438 270 614</p>
  </section>
</body>
</html>
```